Company Postage Label

Design a postage label that measures: 16cm long x 9cm high with a sticky back to stick on boxes. Similar to the attached from Talvora Carriers.

Industry/Entity Type

Motorcycle Part

Colors

Designer to choose colors to be used in the design.

Requirements
Must have
• Company logo and address

```html
<!DOCTYPE html>
<html lang="en">
<head>
<meta charset="utf-8">
<title>Ironpipe Exhaust Specialists – Postage Label</title>
<link href="https://fonts.googleapis.com/css2?family=Oswald:wght@400;500&display=swap" rel="stylesheet">
<style>
  :root {
    --page: #ffffff;
    --frame: #000000;
    --paper: #e9dfc6;
    --paper-edge: #ddd0b2;
    --ink: #111111;
    --ink-soft: #555555;
    --brand-red: #e2242b;
    --sketch: #cfc3a6;
  }
  html, body {
    margin: 0;
    padding: 0;
    width: 1200px;
    height: 1200px;
    overflow: hidden;
    background: var(--page);
  }
  .label {
    display: block;
    width: 1200px;
    height: 1200px;
  }
  .label text {
    font-family: "Oswald", sans-serif;
  }
  .brand-main { fill: var(--brand-red); font-weight: 500; font-size: 60px; }
  .brand-sub { fill: var(--brand-red); font-weight: 400; font-size: 40px; }
  .from-tag { fill: var(--ink-soft); font-size: 21px; }
  .sender-line { fill: var(--ink-soft); font-weight: 500; font-size: 33px; }
  .to-tag { fill: var(--ink-soft); font-size: 26px; font-style: italic; }
  .rule { stroke: var(--ink); stroke-width: 3; }
  .postcode-box { fill: none; stroke: var(--ink); stroke-width: 3; }
  .stamp-box { fill: none; stroke: var(--ink); stroke-width: 1.5; stroke-dasharray: 4 3; }
</style>
</head>
<body>
<svg class="label" viewBox="0 0 1200 1200" xmlns="http://www.w3.org/2000/svg">
  <defs>
    <radialGradient id="paperTone" cx="50%" cy="45%" r="70%">
      <stop offset="0%" stop-color="var(--paper)"/>
      <stop offset="100%" stop-color="var(--paper-edge)"/>
    </radialGradient>
    <linearGradient id="landmarkTone" x1="0" y1="0" x2="0" y2="1">
      <stop offset="0%" stop-color="var(--sketch)" stop-opacity="0"/>
      <stop offset="100%" stop-color="var(--sketch)" stop-opacity="0.7"/>
    </linearGradient>
  </defs>

  <!-- outer frame -->
  <rect class="frame" x="14" y="316" width="1172" height="630" fill="var(--frame)"/>

  <!-- sender panel -->
  <g class="sender-panel">
    <rect x="53" y="355" width="288" height="551" fill="url(#paperTone)"/>
    <text class="from-tag" transform="translate(126 872) rotate(-90)">From</text>
    <text class="brand-main" transform="translate(130 744) rotate(-90)" textLength="224" lengthAdjust="spacingAndGlyphs">Ironpipe</text>
    <text class="brand-sub" transform="translate(174 808) rotate(-90)" textLength="354" lengthAdjust="spacingAndGlyphs">Exhaust Specialists</text>
    <line class="rule" x1="198" y1="381" x2="198" y2="880"/>
    <line class="rule" x1="253" y1="381" x2="253" y2="880"/>
    <line class="rule" x1="308" y1="381" x2="308" y2="880"/>
    <text class="sender-line" transform="translate(238 878) rotate(-90)" textLength="496" lengthAdjust="spacingAndGlyphs">18 Wren Street, Calder Creek, QLD 4199</text>
    <text class="sender-line" transform="translate(296 740) rotate(-90)" textLength="200" lengthAdjust="spacingAndGlyphs">(07) 5550 1427</text>
  </g>

  <!-- recipient panel -->
  <g class="recipient-panel">
    <rect x="360" y="355" width="786" height="551" fill="url(#paperTone)"/>
    <rect class="landmark-sketch" x="360" y="676" width="690" height="230" fill="url(#landmarkTone)" role="img" aria-label="Line sketch of a harbourside opera house with sail-shaped roofs"/>
    <rect class="stamp-box" x="1006" y="379" width="113" height="143"/>
    <text class="to-tag" x="392" y="596">To</text>
    <line class="rule" x1="392" y1="556" x2="1126" y2="556"/>
    <line class="rule" x1="392" y1="618" x2="1126" y2="618"/>
    <line class="rule" x1="392" y1="678" x2="1126" y2="678"/>
    <line class="rule" x1="392" y1="739" x2="1126" y2="739"/>
    <line class="rule" x1="392" y1="800" x2="1126" y2="800"/>
    <g class="postcode">
      <rect class="postcode-box" x="934" y="739" width="190" height="61"/>
      <line class="rule" x1="982" y1="739" x2="982" y2="800"/>
      <line class="rule" x1="1031" y1="739" x2="1031" y2="800"/>
      <line class="rule" x1="1080" y1="739" x2="1080" y2="800"/>
    </g>
  </g>
</svg>
</body>
</html>
```